Simple Business Cards for Self-employed Coach

Simple business card with a design that includes the QLT logo.
Using either only the logo color or additional colors that match the logo.

Meridian Guides reach deeply into the past, gathering wisdom from East and West, while still staying current with the frontiers of new discovery in cognitive science, genetics, and other disciplines. see https://www.brightharborpath.example/what-is-integral-coaching/

Target Market(s)

Coaching Clients in Tokyo /Asia; in business organizations, but also outside

Industry/Entity Type

Life Coaching

Contact Information for Business Card

Lukas Brenning
Certified Meridian Guide

3-2-48 Kamiyoshi
Nakarino 164-0392
Tokyo, Japan

Phone: +81 70 4817 5062
E-Mail: lukas.brenning@mailora.example

Font styles to use
Sans Serif

Colors
00a990

Requirements
Must have
• include uploaded logo
• color fitting with QLT logo color
Nice to have
• simple, elegant design
Should not have
• clutter

```html
<!DOCTYPE html>
<html lang="en">
<head>
<meta charset="utf-8">
<title>QLT Business Card</title>
<link rel="stylesheet" href="https://fonts.googleapis.com/css2?family=Open+Sans:wght@400;600&family=Montserrat:wght@500;700&display=swap">
<style>
  :root {
    --teal: #007a70;
    --silver: #c4c6c9;
    --paper: #ffffff;
    --backdrop: #eceeef;
    --ink-light: #ffffff;
  }
  * { margin: 0; padding: 0; box-sizing: border-box; }
  html, body {
    width: 1200px; height: 900px; overflow: hidden;
    background: var(--backdrop);
  }
  .card {
    position: absolute; left: 112px; top: 150px;
    width: 975px; height: 600px;
    background: var(--paper);
    overflow: hidden;
    box-shadow: 0 6px 24px rgba(0,0,0,0.12);
    font-family: "Open Sans", Arial, sans-serif;
  }
  .card__wave { position: absolute; inset: 0; width: 975px; height: 600px; }
  .brand {
    position: absolute; left: 64px; top: 112px;
    display: flex; align-items: center; gap: 22px;
  }
  .brand__square {
    width: 70px; height: 70px; background: var(--teal);
  }
  .brand__name {
    font-family: "Montserrat", Arial, sans-serif;
    font-weight: 700; font-size: 84px; letter-spacing: 14px;
    color: var(--teal); line-height: 1;
  }
  .contact {
    position: absolute; right: 42px; top: 318px;
    text-align: right; color: var(--ink-light);
  }
  .contact__name { font-weight: 600; font-size: 30px; line-height: 40px; }
  .contact__title { font-size: 25px; line-height: 34px; }
  .contact__line {
    display: flex; justify-content: flex-end; align-items: center;
    gap: 16px; font-size: 24px; line-height: 36px;
  }
  .contact__phone { margin-top: 20px; }
  .contact__line svg { width: 18px; height: 18px; fill: var(--ink-light); }
  .contact__address { margin-top: 32px; font-size: 24px; line-height: 34px; }
</style>
</head>
<body>
  <div class="card">
    <svg class="card__wave" viewBox="0 0 975 600" aria-hidden="true">
      <path fill="var(--silver)" d="M0,290 C160,450 340,472 530,345 C690,238 820,170 975,222 L975,600 L0,600 Z"/>
      <path fill="var(--paper)" d="M0,310 C155,462 335,488 525,368 C685,262 810,210 975,256 L975,600 L0,600 Z"/>
      <path fill="var(--teal)" d="M0,322 C150,474 330,500 520,380 C680,278 805,228 975,270 L975,600 L0,600 Z"/>
    </svg>

    <div class="brand">
      <span class="brand__square"></span>
      <span class="brand__name">QLT</span>
    </div>

    <div class="contact">
      <p class="contact__name">Lukas Brenning</p>
      <p class="contact__title">Certified Meridian Guide</p>
      <p class="contact__line contact__phone">+81 70 4817 5062
        <svg viewBox="0 0 24 24"><path d="M6.6 10.8a15.1 15.1 0 0 0 6.6 6.6l2.2-2.2a1 1 0 0 1 1-.25 11.4 11.4 0 0 0 3.6.57 1 1 0 0 1 1 1V20a1 1 0 0 1-1 1A17 17 0 0 1 3 4a1 1 0 0 1 1-1h3.5a1 1 0 0 1 1 1 11.4 11.4 0 0 0 .57 3.6 1 1 0 0 1-.25 1z"/></svg>
      </p>
      <p class="contact__line">lukas.brenning@mailora.example
        <svg viewBox="0 0 24 24"><path d="M2 5h20v14H2z M4 7v1l8 5 8-5V7l-8 5z" fill-rule="evenodd"/></svg>
      </p>
      <p class="contact__address">3-2-48 Kamiyoshi Nakarino 164-0392 Tokyo, Japan</p>
    </div>
  </div>
</body>
</html>
```